Business card for a plastic surgeon

i need a business card for a plastic surgeon. I have two adresses. The card should communicate safety, simmetry, beauty and with soft colors.
What i want in the card:
- my logo: Letters "R"and "B" (picture uploaded)
- my name: Renato Bastiani
- my registration: CRM 507 219
- my adresses and phone numbers (2):
- Av Dr Teixeira Lopes, 2710, sala 305 - Vila Olímpia | São Paulo/ SP - Phone: 11 4172-5036
- Al. Itapeva, 47, 3 andar - Alphaville | Barueri/ SP - Phone: 11 6350-2481

- my social network: site, facebook and instagram

Target Market(s)

people (95% girls and women) that want cosmetic procedures and plastic surgery

Industry/Entity Type

Business

Contact Information for Business Card

The card should communicate safety, simmetry, beauty and with soft colors.
Beige, brown, gray, rosy are some options. Color is free

Font styles to use
Serif

Requirements
Must have
• - my logo: Letters "R"and "B" (picture uploaded)
• - my name: Renato Bastiani
• - my registration: CRM 507 219
• - my adresses and phone numbers (2):
• - Av Dr Teixeira Lopes, 2710, sala 305 - Vila Olímpia | São Paulo/ SP - Phone: 11 4172-5036
• - Al. Itapeva, 47, 3 andar - Alphaville | Barueri/ SP - Phone: 11 6350-2481
• - my social network: site, facebook and instagram
Should not have
• other images (only my logo)

```html
<!DOCTYPE html>
<html lang="pt-BR">
<head>
<meta charset="utf-8">
<title>Renato Bastiani – Business Card</title>
<link href="https://fonts.googleapis.com/css2?family=Cabin:wght@400;500&family=Cinzel:wght@400&display=swap" rel="stylesheet">
<style>
  :root {
    --backdrop: #d9d9db;
    --card-plum: #3d2f3f;
    --gold: #e6bb5c;
    --mark-faint: rgba(255, 255, 255, 0.09);
    --mark-dark: #141014;
    --rule: #8a7f8c;
  }
  * { margin: 0; padding: 0; box-sizing: border-box; }
  html, body {
    width: 1200px;
    height: 800px;
    overflow: hidden;
    background: var(--backdrop);
  }
  .canvas {
    position: relative;
    width: 1200px;
    height: 800px;
  }
  .card {
    position: absolute;
    left: 344px;
    width: 512px;
    height: 288px;
    border-radius: 18px;
    background: var(--card-plum);
    overflow: hidden;
  }
  .card--front { top: 66px; }
  .card--back { top: 410px; }

  /* Front */
  .front-watermark {
    position: absolute;
    right: 34px;
    top: 30px;
    font-family: "Cinzel", serif;
    font-size: 150px;
    line-height: 1;
    color: var(--mark-faint);
  }
  .contact {
    position: absolute;
    left: 26px;
    top: 108px;
    font-family: "Cabin", sans-serif;
    color: var(--gold);
  }
  .contact__name {
    font-size: 22px;
    font-weight: 400;
    margin-bottom: 8px;
  }
  .contact__line {
    font-size: 12.5px;
    line-height: 17px;
  }
  .contact__site {
    font-size: 14px;
    line-height: 19px;
    margin-top: 2px;
  }
  .contact__registration {
    font-size: 12px;
    line-height: 18px;
  }

  /* Back */
  .back-mark {
    position: absolute;
    left: 0;
    right: 0;
    top: 40px;
    text-align: center;
    font-family: "Cinzel", serif;
    font-size: 76px;
    line-height: 1;
    color: var(--mark-dark);
  }
  .back-name {
    position: absolute;
    left: 0;
    right: 0;
    top: 170px;
    text-align: center;
    font-family: "Cinzel", serif;
    font-size: 21px;
    letter-spacing: 1px;
    color: var(--mark-dark);
  }
  .back-specialty {
    position: absolute;
    left: 0;
    right: 0;
    top: 200px;
    text-align: center;
    font-family: "Cinzel", serif;
    font-size: 10.5px;
    letter-spacing: 4.5px;
    color: var(--mark-dark);
  }
  .back-rule {
    position: absolute;
    left: 0;
    right: 0;
    top: 240px;
    height: 1px;
    background: var(--rule);
  }
</style>
</head>
<body>
<main class="canvas">
  <section class="card card--front" aria-label="Card front">
    <div class="front-watermark" aria-hidden="true">RB</div>
    <div class="contact">
      <p class="contact__name">Renato Bastiani</p>
      <p class="contact__line">Av Dr Teixeira Lopes, 2710,</p>
      <p class="contact__line">sala 305 Vila Olímpia | São Paulo/ SP</p>
      <p class="contact__line">Phone: 11 4172-5036</p>
      <p class="contact__line">Al. Itapeva, 47, 3 andar</p>
      <p class="contact__line">Alphaville | Barueri/ SP</p>
      <p class="contact__line">Phone: 11 6350-2481</p>
      <p class="contact__site">www.renatobastiani-cirurgia.com</p>
      <p class="contact__registration">Registration: CRM 507 219</p>
    </div>
  </section>

  <section class="card card--back" aria-label="Card back">
    <div class="back-mark">RB</div>
    <p class="back-name">DR. RENATO BASTIANI</p>
    <p class="back-specialty">CIRURGIÃO PLÁSTICO</p>
    <div class="back-rule"></div>
  </section>
</main>
</body>
</html>
```